Educational Institution needs a new website

A little bit about ourselves:
Brimley College is a multicultural K-12 school with students who represent nearly 30 ethnic and cultural backgrounds. It is one of the fastest growing schools in the City of Canning (in Perth, Western Australia), and offers quality education with a unique school environment at two campuses.
The mission of Brimley College is to equip students with moral values, academic knowledge and 21st century skills. We empower students to unlock their potential to be confident global citizens.
Brimley College strives to educate students in a manner which inspires them to become lifelong learners. We are committed to raising individuals who are tolerant and respectful towards others enabling them to grow into citizens who contribute to the common good of society.
Here are our design goals:
#1: To emphasise the growth of the school from a small school community to a much larger prestigious college.
#2: Have current and prospective parents have a clear understanding of our college’s morals and values and how we differ from other colleges.
#3: Highlight that our school provides a joyful and safe environment, which is highly valued by parents.
#4: Emphasise that our school presents a welcoming atmosphere for parents as we have strong relationships with our community.
#5: Highlight the various after-school activities available to our students, which are provided through the clubs and pastoral care department.
#6: Allow for online registrations and the option of adding student, staff and parent portals.
#7: Follow the existing school colours
We would like to request the design for the home page and a secondary page to see the alternative layouts.
Other information:
Please note that our logo is will be changed slightly in the upcoming weeks. Please keep this in mind while designing.
We will have another contest for the coding of the website.
We want to be able to make amendments and additions to the content of the website in the future and would like to make sure we have a strong communication with the designer.
The existing website is https://www.brimley-example.edu.au/ for reference for school colours and content.
Education

```html
<!DOCTYPE html>
<html lang="en">
<head>
<meta charset="utf-8">
<title>Brimley College</title>
<link href="https://fonts.googleapis.com/css2?family=Mulish:wght@300;400;600;700;800&family=Poppins:wght@800;900&display=swap" rel="stylesheet">
<style>
:root{
  --sky:#2aa3e0;
  --brand:#1a7fc4;
  --deep:#1a68a8;
  --ink:#333a44;
  --muted:#5b6470;
  --footer:#1f1f21;
  --white:#fff;
  --paper:#f6f6f8;
}
*{box-sizing:border-box;margin:0;padding:0}
html,body{width:1200px;height:4261px;overflow:hidden}
body{font-family:"Mulish",sans-serif;color:var(--ink);background:var(--white);position:relative}
.abs{position:absolute}
a{color:inherit;text-decoration:none}

/* top bar */
.topbar{position:absolute;left:0;top:0;width:1200px;height:28px;background:var(--sky)}
.topbar a{position:absolute;top:7px;font-size:11px;color:var(--white)}
.topbar .sep{position:absolute;top:0;width:1px;height:28px;background:rgba(255,255,255,.5)}

/* header */
.header{position:absolute;left:0;top:28px;width:1200px;height:113px;background:var(--white)}
.brand{position:absolute;left:134px;top:34px;display:flex;align-items:center;gap:10px}
.brand .dot{width:34px;height:34px;background:var(--sky)}
.brand span{font-weight:800;font-size:24px;color:var(--brand);letter-spacing:.5px}
.contact{position:absolute;top:26px;display:flex;align-items:center;gap:12px}
.contact .ic{width:30px;height:30px;border-radius:50%;background:var(--deep);display:flex;align-items:center;justify-content:center}
.contact small{display:block;font-size:10px;color:var(--muted)}
.contact b{display:block;font-size:15px;font-weight:400;color:var(--ink)}
.btn-reg{position:absolute;top:23px;left:811px;width:166px;height:33px;background:var(--deep);color:var(--white);font-size:14px;display:flex;align-items:center;justify-content:center}
.btn-login{position:absolute;top:23px;left:990px;width:79px;height:33px;background:var(--sky);color:var(--white);font-size:14px;display:flex;align-items:center;justify-content:center}
.nav{position:absolute;left:371px;top:75px;display:flex;gap:15px;font-size:12px;color:var(--ink)}
.nav li{list-style:none;display:flex;align-items:center;gap:4px}
.nav li.active{color:var(--brand);font-weight:700;margin-right:8px}

/* hero */
.hero{position:absolute;left:0;top:141px;width:1200px;height:488px;background:linear-gradient(100deg,#3f6e3a 0%,#3a8fc4 30%,#2f6fa2 50%,#4d7a47 75%,#6a6e62 100%)}
.hero h1{position:absolute;left:778px;top:98px;font-family:"Poppins",sans-serif;font-weight:900;font-size:44px;line-height:49px;color:var(--white);text-transform:uppercase}
.hero .btn{left:783px;top:263px}
.dots{position:absolute;left:563px;top:451px;display:flex;gap:8px}
.dots i{width:8px;height:8px;border-radius:50%;background:var(--white)}
.dots i.on{background:var(--sky)}

.btn{position:absolute;background:var(--sky);color:var(--white);font-weight:800;font-size:14px;height:46px;padding:0 22px;display:flex;align-items:center;justify-content:center;text-transform:uppercase}

.heading{position:absolute;left:0;width:1200px;text-align:center;color:var(--brand);font-weight:800;font-size:23px}
.heading::after{content:"";display:block;width:32px;height:3px;background:var(--brand);margin:20px auto 0}

/* learning */
.card{position:absolute;overflow:hidden}
.card .photo{width:100%;height:100%}
.card .cap{position:absolute;left:0;bottom:0;width:100%;height:90px;background:linear-gradient(transparent,rgba(0,0,0,.65));display:flex;align-items:flex-end;padding:0 22px 22px;color:var(--white);font-size:19px;font-weight:600;gap:8px}
.card .cap .line{flex:1;border-bottom:2px dotted rgba(255,255,255,.85);margin-bottom:6px}

/* about */
.about{position:absolute;left:0;top:1270px;width:1200px;height:640px;background:linear-gradient(180deg,#3b3023 0%,#5c6a3d 40%,#8ea93a 75%,#6e7f2f 100%)}
.about .photo{position:absolute;left:136px;top:49px;width:392px;height:523px;background:linear-gradient(180deg,#6a9fd8 0%,#8a5236 45%,#6e6e4a 80%,#4a5a3a 100%)}
.about h2{position:absolute;left:601px;top:55px;color:var(--white);font-weight:800;font-size:24px}
.about h2::after{content:"";display:block;width:32px;height:3px;background:var(--white);margin-top:18px}
.about p{position:absolute;left:599px;top:130px;width:470px;color:var(--white);font-size:14.5px;line-height:20px;font-weight:300}
.stat{position:absolute;width:180px;text-align:center;color:var(--white)}
.stat b{display:block;font-family:"Poppins",sans-serif;font-size:28px;font-weight:800}
.stat span{display:block;font-size:11.5px;line-height:20px;margin-top:4px}
.vline{position:absolute;width:1px;height:170px;background:rgba(255,255,255,.6);top:316px}
.about .btn{left:601px;top:527px}

/* leadership */
.leader-photo{position:absolute;left:131px;top:1966px;width:935px;height:467px;background:linear-gradient(180deg,#6a8a5a 0%,#5b9fc8 55%,#8fc6e6 100%)}
.leader-box{position:absolute;left:175px;top:2319px;width:846px;height:159px;background:var(--white)}
.leader-box h2{position:absolute;left:50px;top:53px;color:var(--brand);font-weight:800;font-size:23px}
.leader-box h2::after{content:"";display:block;width:32px;height:3px;background:var(--brand);margin-top:14px}
.leader-box .bar{position:absolute;left:242px;top:34px;width:2px;height:116px;background:var(--brand)}
.leader-box .txt{position:absolute;left:278px;top:30px;width:540px;font-size:14.5px;line-height:20px;color:var(--ink)}
.leader-box .txt p+p{margin-top:18px}

/* feature band */
.band{position:absolute;left:0;top:2535px;width:1200px;height:583px;background:var(--deep)}
.feature{position:absolute;top:52px;width:444px;color:var(--white)}
.feature .photo{width:444px;height:308px}
.feature h3{font-size:20px;font-weight:600;margin-top:28px}
.feature p{font-size:14.5px;line-height:23px;margin-top:10px;color:#e4eef7}
.feature .btn{position:static;display:inline-flex;margin-top:24px;width:134px}

/* gallery */
.gallery-bg{position:absolute;left:0;top:3118px;width:1200px;height:713px;background:var(--paper)}
.tile{position:absolute;width:229px;height:233px}

/* footer */
.footer{position:absolute;left:0;top:3831px;width:1200px;height:430px;background:var(--footer);color:#d8d8d8}
.fcol{position:absolute;top:45px}
.fcol h4{color:var(--white);font-size:14px;font-weight:700;margin-bottom:8px}
.fcol li{list-style:none;font-size:11.5px;line-height:19.2px}
.footer .rule{position:absolute;left:134px;top:298px;width:935px;height:1px;background:#3a3a3d}
.fbrand{position:absolute;left:134px;top:333px;display:flex;align-items:center;gap:10px}
.fbrand .dot{width:34px;height:34px;background:var(--sky)}
.fbrand span{font-weight:800;font-size:24px;color:var(--sky);letter-spacing:.5px}
.follow{position:absolute;left:869px;top:336px;display:flex;align-items:center;gap:14px;font-size:12px;color:var(--white)}
.follow i{width:30px;height:30px;border-radius:50%;background:var(--white);display:block}
.copy{position:absolute;left:880px;top:376px;font-size:11.5px;color:var(--white)}
</style>
</head>
<body>

<div class="topbar">
  <span class="sep" style="left:886px"></span>
  <span class="sep" style="left:994px"></span>
  <a href="#" style="left:803px">Parent Portal</a>
  <a href="#" style="left:902px">Student portal</a>
  <a href="#" style="left:1011px">Staff Portal</a>
</div>

<header class="header">
  <div class="brand"><div class="dot"></div><span>Brimley College</span></div>
  <div class="contact" style="left:377px">
    <div class="ic"><svg width="14" height="10" viewBox="0 0 14 10"><rect x="0.5" y="0.5" width="13" height="9" fill="none" stroke="#fff"/><path d="M1 1l6 5 6-5" fill="none" stroke="#fff"/></svg></div>
    <div><small>EMAIL US:</small><b style="font-size:14px">admin@brimley-example.edu.au</b></div>
  </div>
  <div class="contact" style="left:642px">
    <div class="ic"><svg width="14" height="14" viewBox="0 0 24 24"><path fill="#fff" d="M6.6 10.8a15 15 0 006.6 6.6l2.2-2.2a1 1 0 011-.25 11.4 11.4 0 003.6.57 1 1 0 011 1V20a1 1 0 01-1 1A17 17 0 013 4a1 1 0 011-1h3.5a1 1 0 011 1c0 1.25.2 2.45.57 3.57a1 1 0 01-.25 1z"/></svg></div>
    <div><small>CALL US:</small><b>(08) 9000 1234</b></div>
  </div>
  <a class="btn-reg" href="#">Online Registrations</a>
  <a class="btn-login" href="#">Login</a>
  <ul class="nav">
    <li class="active">Home</li>
    <li>About Us <svg width="8" height="6"><path d="M1 1l3 3 3-3" fill="none" stroke="#333" stroke-width="1.5"/></svg></li>
    <li>Learning <svg width="8" height="6"><path d="M1 1l3 3 3-3" fill="none" stroke="#333" stroke-width="1.5"/></svg></li>
    <li>Student Life <svg width="8" height="6"><path d="M1 1l3 3 3-3" fill="none" stroke="#333" stroke-width="1.5"/></svg></li>
    <li>Enrolment <svg width="8" height="6"><path d="M1 1l3 3 3-3" fill="none" stroke="#333" stroke-width="1.5"/></svg></li>
    <li>Community <svg width="8" height="6"><path d="M1 1l3 3 3-3" fill="none" stroke="#333" stroke-width="1.5"/></svg></li>
    <li>News &amp; Events <svg width="8" height="6"><path d="M1 1l3 3 3-3" fill="none" stroke="#333" stroke-width="1.5"/></svg></li>
    <li>Contact Us <svg width="8" height="6"><path d="M1 1l3 3 3-3" fill="none" stroke="#333" stroke-width="1.5"/></svg></li>
  </ul>
</header>

<section class="hero" role="img" aria-label="Photo of smiling students in light blue uniforms on a playground">
  <h1>Welcome to<br>Brimley<br>College</h1>
  <a class="btn" href="#">Read More</a>
  <div class="dots"><i></i><i></i><i class="on"></i><i></i><i></i></div>
</section>

<h2 class="heading" style="top:666px">LEARNING</h2>
<div class="card" style="left:134px;top:743px;width:313px;height:434px">
  <div class="photo" role="img" aria-label="Photo of a kindergarten child painting" style="background:linear-gradient(160deg,#c9d6dc,#7fb8d8 50%,#b07a62)"></div>
  <div class="cap">Kindergarten <span class="line"></span><svg width="12" height="20"><path d="M2 2l8 8-8 8" fill="none" stroke="#fff" stroke-width="3"/></svg></div>
</div>
<div class="card" style="left:447px;top:781px;width:311px;height:434px">
  <div class="photo" role="img" aria-label="Photo of a student looking through a microscope" style="background:linear-gradient(160deg,#2d3238,#5a6168 40%,#7fb0d0 75%,#d8d8d8)"></div>
  <div class="cap">Primary Curriculum <span class="line"></span><svg width="12" height="20"><path d="M2 2l8 8-8 8" fill="none" stroke="#fff" stroke-width="3"/></svg></div>
</div>
<div class="card" style="left:758px;top:743px;width:311px;height:434px">
  <div class="photo" role="img" aria-label="Photo of students building with blocks alongside a teacher" style="background:linear-gradient(160deg,#8fae4a,#5f7a6a 40%,#7b8894 75%,#9a9a9a)"></div>
  <div class="cap">Secondary Curriculum <span class="line"></span><svg width="12" height="20"><path d="M2 2l8 8-8 8" fill="none" stroke="#fff" stroke-width="3"/></svg></div>
</div>

<section class="about">
  <div class="photo" role="img" aria-label="Photo of the red brick heritage college building with students outside"></div>
  <h2>ABOUT US</h2>
  <p>We at Brimley College are constantly in search of better ways to educate and prepare our students for life in the 21st century, where we believe that only individuals with soft skills (such as creativity, collaboration, communication and critical thinking) will be able to reach their full potential. Although this is a challenging aim, education is not a formidable matter as long as you are devoted enough. In my opinion, it is all about love and care.</p>
  <div class="vline" style="left:753px"></div>
  <div class="vline" style="left:948px"></div>
  <div class="stat" style="left:569px;top:314px"><b>16</b><span>Average Class Size</span></div>
  <div class="stat" style="left:756px;top:314px"><b>2:0</b><span>Teacher/Student Ratio</span></div>
  <div class="stat" style="left:929px;top:314px"><b>50</b><span>Clubs &amp; Sports</span></div>
  <div class="stat" style="left:569px;top:411px"><b>100%</b><span>Acceptance Rate<br>to College</span></div>
  <div class="stat" style="left:756px;top:411px"><b>$5</b><span>Million in<br>Scholarships</span></div>
  <div class="stat" style="left:929px;top:411px"><b>25</b><span>Years of<br>Excellence</span></div>
  <a class="btn" href="#">Read More</a>
</section>

<div class="leader-photo" role="img" aria-label="Group photo of student leaders and a staff member outdoors"></div>
<div class="leader-box">
  <h2>LEADERSHIP</h2>
  <div class="bar"></div>
  <div class="txt">
    <p>Brimley College is a great place for aspiring leaders. There are vast opportunities to nurture student leaders like SRC, pastoral care programs, mentoring, factions and programs embedded in the curriculum.</p>
    <p>There are SRC representatives from each class from year 6 to 12 and school captains are elected among year 12 students.</p>
  </div>
</div>

<section class="band">
  <div class="feature" style="left:134px">
    <div class="photo" role="img" aria-label="Photo of two students using a tablet" style="background:linear-gradient(150deg,#5a4a3a,#8fb7d9 50%,#2f4fa0)"></div>
    <h3>Online Learning</h3>
    <p>Brimley College is implementing the following online learning and assessment...</p>
    <a class="btn" href="#">Read More</a>
  </div>
  <div class="feature" style="left:624px">
    <div class="photo" role="img" aria-label="Photo of students around an interactive projection table" style="background:linear-gradient(160deg,#6a5a48,#3a4a68 45%,#9ed0f0)"></div>
    <h3>Clubs</h3>
    <p>Here at Brimley College, clubs focus on students having fun and building friendships, learning skills or...</p>
    <a class="btn" href="#">Read More</a>
  </div>
</section>

<div class="gallery-bg"></div>
<h2 class="heading" style="top:3167px">GALLERY</h2>
<div class="tile" style="left:132px;top:3247px;background:linear-gradient(160deg,#4a6a4a,#8a3a3a)" role="img" aria-label="Photo of a student on a red tractor"></div>
<div class="tile" style="left:367px;top:3247px;background:linear-gradient(160deg,#3f7fb0,#7cc0e6)" role="img" aria-label="Photo of young students in school hats"></div>
<div class="tile" style="left:602px;top:3247px;background:linear-gradient(160deg,#c8c4a8,#7fbfe0)" role="img" aria-label="Photo of students working in class"></div>
<div class="tile" style="left:839px;top:3247px;background:linear-gradient(160deg,#c88a7a,#8fcbe8)" role="img" aria-label="Photo of a teacher walking with a student"></div>
<div class="tile" style="left:132px;top:3489px;background:linear-gradient(160deg,#7a6a52,#6fa8c8)" role="img" aria-label="Photo of students measuring outdoors"></div>
<div class="tile" style="left:367px;top:3489px;background:linear-gradient(160deg,#d8d8d8,#2a2f3a)" role="img" aria-label="Photo of a student in a lab coat"></div>
<div class="tile" style="left:602px;top:3489px;background:linear-gradient(160deg,#b07050,#3a3a3a 50%,#80c0e0)" role="img" aria-label="Photo of a student writing at a desk"></div>
<div class="tile" style="left:839px;top:3489px;background:linear-gradient(160deg,#2a3a58,#90c8e8)" role="img" aria-label="Photo of a teacher with a young student"></div>
<a class="btn" href="#" style="left:535px;top:3752px;width:132px">Read More</a>

<footer class="footer">
  <div class="fcol" style="left:134px"><h4>About Us</h4><ul><li>Principal's Message</li><li>School Philosophy</li><li>School Emblem</li><li>History</li><li>Governance</li><li>Prospectus</li><li>Policies</li><li>Annual Report</li><li>Organisation Chart</li></ul></div>
  <div class="fcol" style="left:306px"><h4>Learning</h4><ul><li>Early Years</li><li>Primary</li><li>Middle Years</li><li>Senior Secondary</li><li>Extracurricular / Co-curricular</li><li>STEAM Education</li><li>Online Learning</li></ul></div>
  <div class="fcol" style="left:531px"><h4>Student Life</h4><ul><li>Learning Support</li><li>Career Guidance</li><li>Counselling</li><li>Youth Award</li><li>Student Leadership</li><li>Library</li><li>Pastoral Care</li></ul></div>
  <div class="fcol" style="left:725px"><h4>Enrolment</h4><ul><li>Enrolment Procedures</li><li>School Fees</li><li>Scholarships</li><li>International Students</li><li>Transport Facilities</li><li>Canteen Facilities</li><li>Book Lists &amp; Suppliers</li><li>School Uniform</li><li>Enrolment Application</li></ul></div>
  <div class="fcol" style="left:930px"><h4>News &amp; Events</h4><ul><li>Events</li><li>Newsletters</li><li>Academic Calendar</li><li>Major Dates</li><li>Photo Gallery</li><li>Video Gallery</li><li>STEAM Fest</li><li>Drama Night</li><li>Open Days</li><li>Parent Teacher Interviews</li></ul></div>
  <div class="rule"></div>
  <div class="fbrand"><div class="dot"></div><span>Brimley College</span></div>
  <div class="follow">Follow us <i aria-label="Social link"></i><i aria-label="Social link"></i><i aria-label="Social link"></i></div>
  <div class="copy">Copyright © 2023 All Rights Reserved</div>
</footer>

</body>
</html>
```